Novu Staffing Tri Fold Brochure

My company is a recruiting/staffing firm. I need a design that is going to be professional, bright, young, hip and fun. Pictures are key! We want people working in an office, packaging, food production and/or light industrial environment. Must embrace DIVERSITY. Please use the 4 primary colors from the Novu Logo to accent the piece, but not too busy. I am including the content that I would like to be included in the trifold as well as a sample of a trifold I have used in the past in addition to a couple of logos. My website is www.NovuStaffing.example for look and feel.

Target Market(s)

Logistics, Distribution and Manufacturing companies

Industry/Entity Type

Staffing

Requirements
Must have
• Clean, colorful, eye catching, great pictures and graphics. Photo's of diverse people working, in a office, or production setting.
Nice to have
• Must be professional
Should not have
• Not too busy.

```html
<!DOCTYPE html>
<html lang="en">
<head>
<meta charset="utf-8">
<title>Novu Staffing Tri-Fold Brochure</title>
<link href="https://fonts.googleapis.com/css2?family=Montserrat:wght@600;700;800&family=Open+Sans:ital,wght@0,400;0,600;1,400&display=swap" rel="stylesheet">
<style>
:root{
  --navy:#2b2a7c;
  --yellow:#dcb513;
  --green:#1d7d3b;
  --red:#e2262b;
  --ink:#333;
  --paper:#fff;
  --bg:#5d6066;
}
*{box-sizing:border-box;margin:0;padding:0}
html,body{width:1200px;height:1200px;overflow:hidden;background:var(--bg);font-family:"Open Sans",Arial,sans-serif;color:var(--ink)}
.spread{position:absolute;left:220px;width:760px;height:580px;display:flex;background:var(--paper);box-shadow:0 6px 18px rgba(0,0,0,.35)}
.spread--outside{top:12px}
.spread--inside{top:608px}
.panel{position:relative;width:253.33px;height:580px;overflow:hidden;border-right:1px solid #e6e6e6}
.panel:last-child{border-right:none}
.panel svg.bg{position:absolute;inset:0;width:100%;height:100%}
.content{position:absolute}
.heading{font-family:"Montserrat",Arial,sans-serif;font-weight:800;color:var(--navy);font-size:13px;border-left:3px solid var(--yellow);padding-left:5px;line-height:1.1;margin-bottom:5px}
.body{font-size:7px;line-height:1.45;text-align:justify}
.body--italic{font-style:italic}
.body + .heading{margin-top:10px}
.body + .body{margin-top:6px}
.brand{font-family:"Montserrat",Arial,sans-serif;font-weight:700;color:var(--navy);font-size:24px;letter-spacing:.5px;display:flex;align-items:center;gap:5px}
.brand .dot{width:8px;height:8px;border-radius:50%;background:var(--green)}
.brand--light{color:#fff}
/* locations */
.locations{left:14px;top:290px;width:228px;color:#fff}
.locations h3{font-family:"Montserrat",Arial,sans-serif;font-size:12px;text-align:center;margin-bottom:6px}
.loc{display:flex;align-items:flex-start;gap:6px;margin-bottom:6px}
.pill{background:var(--yellow);color:#fff;font-family:"Montserrat",Arial,sans-serif;font-weight:700;font-size:6.5px;border-radius:8px;padding:2px 6px;white-space:nowrap;min-width:62px;text-align:center}
.loc ul{list-style:none;font-size:6.5px;line-height:1.4;margin-left:auto;text-align:right}
/* contact */
.contact{left:0;width:253px;text-align:center}
.contact .item{margin-top:18px;font-size:8px}
.contact .item svg{display:block;margin:0 auto 4px}
.contact .phone{font-family:"Montserrat",Arial,sans-serif;font-weight:700;font-size:12px}
/* cover */
.definition{right:14px;top:395px;width:225px;text-align:right}
.definition .url{font-size:7px;color:var(--red);margin-bottom:4px}
.definition h1{font-family:"Montserrat",Arial,sans-serif;font-weight:800;color:var(--green);font-size:19px;line-height:1.05}
.definition h2{font-family:"Montserrat",Arial,sans-serif;font-weight:700;font-size:9.5px;color:#222;margin-top:4px;line-height:1.3}
.definition .rule{display:inline-block;width:40px;height:3px;background:var(--red);margin:6px 0}
.definition p{font-size:9.5px;line-height:1.35;color:#222}
/* inside */
.options-title{margin-top:12px}
.tag{display:inline-block;color:#fff;font-family:"Montserrat",Arial,sans-serif;font-weight:700;font-size:7.5px;padding:3px 14px 3px 8px;clip-path:polygon(0 0,88% 0,100% 50%,88% 100%,0 100%);margin:8px 0 4px}
.tag--red{background:var(--red)}
.tag--green{background:var(--green)}
.tag--navy{background:var(--navy)}
.sector{margin-bottom:12px}
.sector .heading{font-size:11px}
.cols{display:flex;gap:8px}
.cols ul{list-style:none;font-size:6.8px;line-height:1.5;flex:1}
.cols li::before{content:"";display:inline-block;width:5px;height:5px;border-radius:50%;background:var(--red);margin-right:4px;vertical-align:middle}
.site{color:#fff;font-size:8px;position:absolute;right:14px;bottom:20px}
</style>
</head>
<body>

<section class="spread spread--outside">
  <div class="panel">
    <svg class="bg" viewBox="0 0 253 580" preserveAspectRatio="none">
      <defs>
        <linearGradient id="photoA" x1="0" y1="0" x2="1" y2="0"><stop offset="0" stop-color="#9aa3ad"/><stop offset=".55" stop-color="#6b6f76"/><stop offset=".6" stop-color="#b8322e"/><stop offset="1" stop-color="#8e1f1f"/></linearGradient>
        <linearGradient id="photoB" x1="0" y1="0" x2="1" y2="1"><stop offset="0" stop-color="#c9b79f"/><stop offset="1" stop-color="#3d2c22"/></linearGradient>
      </defs>
      <polygon points="0,200 253,185 253,265 0,300" fill="url(#photoA)" role="img" aria-label="Photo of a smiling businesswoman at an office meeting"/>
      <polygon points="0,300 253,265 253,470 0,440" fill="var(--green)"/>
      <polygon points="0,440 253,470 253,580 0,580" fill="url(#photoB)" role="img" aria-label="Photo of a thoughtful professional holding a pen"/>
    </svg>
    <div class="content" style="left:14px;top:18px;width:225px">
      <div class="heading" style="font-size:12px">Onsite Management</div>
      <p class="body body--italic">NOVU Staffing offers Onsite Management for clients that utilize a high volume of Novu associates. Our Onsite Manager will in essence serve as an extension of our client's management team. They are on the production floor 75% of the time, not in an office. NOVU Staffing's Onsite Manager is charged with training Novu Associates, coaching, counseling, driving production as well as quality and overall safety.</p>
      <div class="brand" style="margin-top:14px;justify-content:center;font-size:20px"><span class="dot"></span>Novu Staffing</div>
    </div>
    <div class="content locations">
      <h3>Locations</h3>
      <div class="loc"><span class="pill">Georgia</span><ul><li>Riverton - 555-010-4821</li><li>Oakmere - 555-010-3371</li><li>Bayfield - 555-010-6838</li><li>Linden Cross - 555-010-0735</li></ul></div>
      <div class="loc"><span class="pill">Pennsylvania</span><ul><li>Stonebrook - 555-010-3700</li><li>Fairhaven - 555-010-6799</li></ul></div>
      <div class="loc"><span class="pill">Indiana</span><ul><li>Westvale - 555-010-8558</li></ul></div>
      <div class="loc"><span class="pill">Texas</span><ul><li>Redmesa - 555-010-4570</li></ul></div>
    </div>
  </div>

  <div class="panel">
    <svg class="bg" viewBox="0 0 253 580" preserveAspectRatio="none">
      <path d="M0,0H253V30Q130,70 0,55Z" fill="var(--yellow)"/>
      <path d="M0,580V500Q140,470 253,420V580Z" fill="var(--yellow)"/>
    </svg>
    <div class="content" style="left:0;top:78px;width:253px;display:flex;justify-content:center">
      <div class="brand"><span class="dot"></span>Novu Staffing</div>
    </div>
    <div class="content contact" style="top:130px">
      <div class="item">
        <svg width="14" height="14" viewBox="0 0 14 14"><circle cx="7" cy="7" r="7" fill="var(--navy)"/><path d="M7 3.2a2.4 2.4 0 0 0-2.4 2.4c0 1.8 2.4 4.6 2.4 4.6s2.4-2.8 2.4-4.6A2.4 2.4 0 0 0 7 3.2z" fill="#fff"/><circle cx="7" cy="5.6" r=".9" fill="var(--navy)"/></svg>
        450 Harbor View Ave, Suite 210, Riverton,<br>GA 30199
      </div>
      <div class="item">
        <svg width="14" height="14" viewBox="0 0 14 14"><circle cx="7" cy="7" r="7" fill="var(--navy)"/><path d="M4.6 3.6l1.3-.3.8 1.9-.9.7a5 5 0 0 0 2.3 2.3l.7-.9 1.9.8-.3 1.3c-3.3.3-6.1-2.5-5.8-5.8z" fill="#fff"/></svg>
        <span class="phone">555-010-4821 OFFICE</span>
      </div>
      <div class="item">
        <svg width="14" height="14" viewBox="0 0 14 14"><circle cx="7" cy="7" r="7" fill="var(--navy)"/><g fill="none" stroke="#fff" stroke-width=".8"><circle cx="7" cy="7" r="3.5"/><ellipse cx="7" cy="7" rx="1.5" ry="3.5"/><path d="M3.5 7h7"/></g></svg>
        www.NovuStaffing.example
      </div>
    </div>
  </div>

  <div class="panel">
    <svg class="bg" viewBox="0 0 253 580" preserveAspectRatio="none">
      <defs>
        <linearGradient id="photoC" x1="0" y1="0" x2="1" y2="1"><stop offset="0" stop-color="#dcdfe3"/><stop offset=".5" stop-color="#6a6f78"/><stop offset="1" stop-color="#2e3038"/></linearGradient>
      </defs>
      <rect x="0" y="20" width="253" height="340" fill="url(#photoC)" role="img" aria-label="Photo of a smiling businessman offering a handshake in front of a diverse team"/>
      <path d="M70,0H253V140Q180,90 70,0Z" fill="var(--navy)"/>
      <path d="M0,0H70Q100,20 0,30Z" fill="var(--yellow)"/>
      <path d="M0,300Q140,320 253,340V380Q140,350 0,345Z" fill="var(--yellow)"/>
      <path d="M0,345Q140,350 253,380V580H0Z" fill="var(--paper)"/>
    </svg>
    <div class="content" style="right:18px;top:30px">
      <div class="brand brand--light" style="font-size:28px">Novu</div>
    </div>
    <div class="content definition">
      <div class="url">www.NovuStaffing.example</div>
      <h1>DEFINITION<br>OF NOVU – VERB</h1>
      <h2>TO BE IN HARMONY OR ACCORD;<br>TO FIT; AGREE</h2>
      <span class="rule"></span>
      <p>“Yes, the candidate meets the requirements, yeah, they have the skills, but do they Novu?”</p>
    </div>
  </div>
</section>

<section class="spread spread--inside">
  <div class="panel">
    <svg class="bg" viewBox="0 0 253 580" preserveAspectRatio="none">
      <path d="M0,580V548Q130,540 253,520V580Z" fill="var(--yellow)"/>
    </svg>
    <div class="content" style="left:14px;top:18px;width:225px">
      <div class="heading">Mission</div>
      <p class="body">At NOVU Staffing, we are passionate in our pursuit to change lives by connecting great people with great organizations.</p>
      <div class="heading">Who We Are</div>
      <p class="body">At NOVU Staffing, we are interested in helping people and improving lives. We partner with great organizations who are looking to make themselves even better by placing driven and passionate individuals interested in improving their lives and careers. NOVU Staffing is a values-based organization that approaches every interaction with integrity and strives to ensure that every placement makes a positive impact.</p>
      <div class="heading">What We Do</div>
      <p class="body">At NOVU Staffing we do things a little differently. We don't just act as a pipeline, blindly pumping workers into your organization who exit almost as quickly as they appear. We provide a system of professional development and training that prepares our talent to enter each placement with the skills and the attitude they need to succeed. In addition to our years of light industrial and professional staffing experience, Novu Staffing is also a leader in creating client specific onsite programs and high-volume recruitment programs that are designed to meet the specific needs of our individual clients.</p>
      <p class="body">We believe in providing our partners with not only the most prepared talent, but also the most secure. At NOVU Staffing, we do more than simply satisfy the minimum legal requirements for screening. We incorporate an extensive battery of tests and checks, including background and drug, as well as ensuring that every individual we recommend and place is work-eligibility verified.</p>
      <p class="body">NOVU Staffing is powered by a recruiting engine that never stops. With the right combination of passion and process, we not only have the motivation to meet the Temporary Staffing, Temp-to-Hire and Direct Hire needs of great companies, but we also have the resources and experience to deliver on the promise of a better experience. We provide a higher level of service through our on-boarding and pre-training programs, which are designed to maximize the value of our placements.</p>
    </div>
  </div>

  <div class="panel">
    <svg class="bg" viewBox="0 0 253 580" preserveAspectRatio="none">
      <path d="M0,580V520Q130,515 253,500V580Z" fill="var(--yellow)"/>
    </svg>
    <div class="content" style="left:14px;top:18px;width:225px">
      <p class="body">At NOVU Staffing, we have a golden opportunity to positively impact the lives of employers and job seekers. This opportunity is a privilege and an honor and is why we love what we do.</p>
      <p class="body">We look forward to learning about your specific needs and exploring how NOVU Staffing can bring immediate and lasting value.</p>
      <div class="heading options-title">Staffing Options</div>
      <span class="tag tag--red">Temporary</span>
      <p class="body">This is an ideal solution that provides flexibility for companies that may have projects, seasonal spikes or a need to fill in the gaps when job vacancies occur. It is a great way for companies to ramp up without adding new associates to the payroll. It also saves on associate costs and provides an opportunity to evaluate talent.</p>
      <span class="tag tag--green">Temp to Hire</span>
      <p class="body">Is a way for clients to test the waters and see if the candidate will prove themselves and be a good long-term fit with the company. This program enables the client to examine the performance and attitude of the candidate for a predetermined period of time while on Novu's payroll prior to being offered a full-time position with the client.</p>
      <span class="tag tag--navy">Direct Hire</span>
      <p class="body">When a client has a long-term or highly skilled need, direct hire is an ideal program. Many top performers will not leave a full-time job for a temp or temp to hire opportunity. This is a great way for companies to attract top talent! Novu will recruit and screen candidates to be interviewed with the client. When the client chooses to move forward and offer a full-time position, the candidate will go directly on the client's payroll and become a full-time associate on day 1.</p>
      <div class="brand" style="margin-top:14px;justify-content:center"><span class="dot"></span>Novu Staffing</div>
    </div>
  </div>

  <div class="panel">
    <svg class="bg" viewBox="0 0 253 580" preserveAspectRatio="none">
      <defs>
        <linearGradient id="photoD" x1="0" y1="0" x2="1" y2="1"><stop offset="0" stop-color="#e7e9ec"/><stop offset=".6" stop-color="#8f949b"/><stop offset="1" stop-color="#3b3e45"/></linearGradient>
      </defs>
      <rect x="0" y="0" width="253" height="170" fill="url(#photoD)" role="img" aria-label="Photo of a diverse team meeting around an office table"/>
      <path d="M0,190Q130,150 253,130V155Q130,165 0,205Z" fill="var(--yellow)"/>
      <path d="M0,205Q130,165 253,155V170H0Z" fill="var(--paper)"/>
      <path d="M0,580V560Q150,520 253,460V580Z" fill="var(--navy)"/>
    </svg>
    <div class="content" style="left:14px;top:200px;width:228px">
      <div class="sector">
        <div class="heading">Light Industrial</div>
        <div class="cols">
          <ul><li>Manufacturing</li><li>Logistics</li><li>Packaging</li><li>Assembly</li></ul>
          <ul><li>Printing</li><li>Fulfillment</li><li>Hospitality</li></ul>
        </div>
      </div>
      <div class="sector">
        <div class="heading">Skilled Trades</div>
        <div class="cols">
          <ul><li>Electrical</li><li>Maintenance</li><li>Welding</li><li>Painting</li></ul>
          <ul><li>C&amp;C Operators/ Programmers</li><li>Machine Operators</li><li>Plumbing</li></ul>
        </div>
      </div>
      <div class="sector">
        <div class="heading">Professional</div>
        <div class="cols">
          <ul><li>Accounting</li><li>Administrative</li><li>Call Center</li><li>Customer Service</li></ul>
          <ul><li>Data Entry</li><li>Executive Management</li><li>Legal</li><li>Sales</li></ul>
        </div>
      </div>
    </div>
    <span class="site">www.NovuStaffing.example</span>
  </div>
</section>

</body>
</html>
```